Icon-Design für Terminmanagement Start-Up
Sehr gute, schnelle, kreative Arbeit. Vielen Dank!
Zielgruppe
Wir sind ein Startup, das über die Seite Kalendora.de zukünftig folgenden Service anbietet: Unternehmer können sehr flexibel (selbst) gestaltete Terminformulare erstellen und auf Ihrer Website einbinden. Kunden können dann diese Termine buchen und bekommen dann Erinnerungs-Mails und SMS.
Zielgruppe: Dienstleister wie Fotografen, Friseure, Versicherungsvertreter, Masseure, Restaurants, Arztpraxen. Also alle, die darauf angewiesen sind, dass vereinbarte Termine eingehalten werden und die die Terminvereinbarung vereinfachen wollen. Also weniger per Telefon, mehr über die eigene Website.
Dateien bitte beachten für die Ansicht des Look & Feels:
https://ablage.wolkenfach.de/open?id=7QmrtuKWZ3fdN84s2Lp9xRbVoE6cJHT_
Bonus-Aktion: Wir zahlen pauschal jeweils 25,00 Euro an die Designer auf den Plätzen 2 bis 5 für die geleistete Arbeit. Nur einer kann gewinnen und den Zuschlag bekommen. Aber so möchten wir gerne die Arbeit dennoch honorieren.
Weitere Icons für die Usability-Unterstützung sowie für weitere Branchen würden wir dann anschließend beim Designer/Gewinner in Auftrag geben für Kalendora und auch Top-oder-Flop.com (weiteres Projekt, das mit Kalendora verbunden ist).
Aufgabenstellung
Im Rahmen der Icon-Ausschreibung reichen uns erstmal folgende fünf Zielgruppen:
- Restaurants
- Ärzte
- Friseure
- Kosmetik-Salons
- Versicherungsbüros

```html
<!DOCTYPE html>
<html lang="de">
<head>
<meta charset="utf-8">
<title>Kalendora – Branchen</title>
<link href="https://fonts.googleapis.com/css2?family=Jost:wght@400;500;600&display=swap" rel="stylesheet">
<style>
  :root {
    --bg: #ffffff;
    --ink: #6b767a;
    --ink-soft: #8a9296;
    --green: #8dc043;
    --green-light: #b5d88a;
    --grey-icon: #7a8387;
    --card: #ffffff;
  }
  * { box-sizing: border-box; margin: 0; padding: 0; }
  html, body {
    width: 1200px; height: 848px; overflow: hidden;
    background: var(--bg);
    font-family: "Jost", "Futura", sans-serif;
    color: var(--ink);
  }
  .page { position: relative; width: 1200px; height: 848px; }

  .industry-card {
    position: absolute;
    width: 127px; height: 102px;
    background: var(--card);
    border-radius: 10px;
    box-shadow: 0 14px 30px rgba(60, 70, 75, 0.10), 0 2px 6px rgba(60, 70, 75, 0.04);
    display: flex; align-items: center; justify-content: center;
  }
  .industry-icon {
    width: 72px; height: 68px;
    border-radius: 8px;
    background: linear-gradient(135deg, var(--green-light) 0%, #c9cfd1 60%, var(--grey-icon) 100%);
    opacity: 0.55;
  }
  .card-hair { left: 344px; top: 90px; }
  .card-cosmetics { left: 117px; top: 179px; }
  .card-restaurant { left: 401px; top: 276px; }
  .card-insurance { left: 215px; top: 360px; }
  .scheduling-icon {
    position: absolute; left: 283px; top: 236px;
    width: 79px; height: 79px; border-radius: 50%;
    background: linear-gradient(135deg, var(--green-light), var(--green));
    opacity: 0.5;
  }

  .feature {
    position: absolute; left: 633px; top: 131px; width: 420px;
  }
  .feature-title {
    font-weight: 500; font-size: 27px; line-height: 32px;
    letter-spacing: 0.1px; color: var(--ink);
  }
  .feature-text {
    margin-top: 37px;
    font-size: 12.5px; line-height: 24px; color: var(--ink-soft);
    width: 345px;
  }
  .btn-outline {
    display: flex; align-items: center; justify-content: center;
    margin-top: 36px;
    width: 187px; height: 50px;
    border: 1px solid var(--green); border-radius: 2px;
    font-size: 12.5px; font-weight: 500; color: var(--ink);
    text-decoration: none; letter-spacing: 0.2px;
  }

  .signup {
    position: absolute; left: 0; top: 596px; width: 1200px;
    text-align: center;
  }
  .signup-title {
    font-weight: 500; font-size: 20px; line-height: 32px; color: var(--ink);
  }
  .signup-text {
    margin: 14px auto 0; width: 520px;
    font-size: 12.5px; line-height: 24px; color: var(--ink-soft);
  }
  .btn-primary {
    display: flex; align-items: center; justify-content: center;
    margin: 40px auto 0;
    width: 354px; height: 50px;
    background: var(--green); border-radius: 2px;
    color: #fff; font-size: 12.5px; font-weight: 600; text-decoration: none;
  }
</style>
</head>
<body>
<main class="page">
  <section class="industries" aria-label="Branchen">
    <div class="industry-card card-hair"><div class="industry-icon" role="img" aria-label="Icon Friseur: Haarschnitt mit Kamm"></div></div>
    <div class="industry-card card-cosmetics"><div class="industry-icon" role="img" aria-label="Icon Kosmetik-Salon: Lippenstift, Mascara und Spiegel"></div></div>
    <div class="scheduling-icon" role="img" aria-label="Icon Terminplanung: Wecker mit Zahnrad"></div>
    <div class="industry-card card-restaurant"><div class="industry-icon" role="img" aria-label="Icon Restaurant: Servierglocke mit Besteck"></div></div>
    <div class="industry-card card-insurance"><div class="industry-icon" role="img" aria-label="Icon Versicherungsbüro: Haus in schützenden Händen"></div></div>
  </section>

  <section class="feature">
    <h2 class="feature-title">Detaillierte Termin-Einstellungen für jeden Anwendungszweck – Branchenübergreifend.</h2>
    <p class="feature-text">Lorem ipsum dolor sit amet, consetetur sadipscing elitr, sed diam nonumy eirmod tempor invidunt ut labore et dolore magna aliquyam erat, sed diam voluptua. At vero eos et accusam et justo duo dolores et ea rebum. Stet clita kasd</p>
    <a class="btn-outline" href="#">Mehr erfahren</a>
  </section>

  <section class="signup">
    <h2 class="signup-title">Jetzt kostenlos registrieren und<br>von Kalendora profitieren</h2>
    <p class="signup-text">Lorem ipsum dolor sit amet, consetetur sadipscing elitr, sed diam nonumy eirmod tempor invidunt ut labore et dolore magna aliquyam erat, sed diam voluptua. At vero eos et accusam et justo duo dolores et ea rebum.</p>
    <a class="btn-primary" href="#">Jetzt kostenlos Konto erstellen</a>
  </section>
</main>
</body>
</html>
```